Navelo Partnering Business Card

Hello everyone. We need a business card design that would match our logo and the theme we're trying to have for Navelo that you can find on our website and/or Corvapage page

```html
<!DOCTYPE html>
<html lang="en">
<head>
<meta charset="utf-8">
<title>Navelo Partnering – Business Card</title>
<link rel="stylesheet" href="https://fonts.googleapis.com/css2?family=Lato:wght@400;700&family=Lexend:wght@600&display=swap">
<style>
  :root {
    --purple: #35215a;
    --purple-deep: #1b1230;
    --ink: #1f1a2b;
    --white: #ffffff;
    --page: #ffffff;
    --card-shadow: rgba(0, 0, 0, 0.22);
  }
  * { box-sizing: border-box; margin: 0; padding: 0; }
  html, body {
    width: 1200px; height: 1200px; overflow: hidden;
    background: var(--page);
    font-family: "Lato", Arial, sans-serif;
  }
  .canvas { position: relative; width: 1200px; height: 1200px; }

  .card {
    position: absolute; left: 254px; width: 692px; height: 396px;
    border-radius: 36px; overflow: hidden;
    box-shadow: 0 0 14px var(--card-shadow);
  }
  .card--front { top: 162px; background: var(--white); }
  .card--back  { top: 592px; background: var(--purple); }

  .front-wave { position: absolute; inset: 0; width: 692px; height: 396px; }

  .details { position: absolute; inset: 0; color: var(--ink); }
  .line {
    position: absolute; right: 338px; white-space: nowrap;
    font-size: 17px; line-height: 20px; text-align: right;
  }
  .line--icon { right: 366px; }
  .holder-name {
    position: absolute; right: 338px; top: 88px;
    font-family: "Lexend", Arial, sans-serif; font-weight: 600;
    font-size: 23px; letter-spacing: 0.5px; color: var(--purple);
  }
  .holder-role { top: 116px; }
  .addr-1 { top: 152px; }
  .addr-2 { top: 175px; }
  .phone  { top: 214px; }
  .email  { top: 238px; }
  .web    { top: 262px; }

  .contact-icon {
    position: absolute; left: 338px; width: 16px; height: 16px;
  }
  .contact-icon--phone { top: 216px; }
  .contact-icon--mail  { top: 240px; }
  .contact-icon--web   { top: 264px; }

  .divider { position: absolute; left: 373px; width: 2px; background: var(--ink); }
  .divider--name { top: 90px; height: 43px; }
  .divider--addr { top: 156px; height: 32px; }
  .divider--contact { top: 216px; height: 73px; }

  .brand {
    position: absolute; display: flex; align-items: center; gap: 10px;
    font-family: "Lato", Arial, sans-serif; font-weight: 700;
  }
  .brand-dot { border-radius: 50%; flex: none; }
  .brand--front { left: 420px; top: 150px; font-size: 44px; color: var(--purple); }
  .brand--front .brand-dot { width: 16px; height: 16px; background: var(--purple); }
  .brand--back {
    left: 0; right: 0; top: 150px; justify-content: center;
    font-size: 84px; color: var(--white);
  }
  .brand--back .brand-dot { width: 26px; height: 26px; background: var(--white); }

  .back-flow {
    position: absolute; inset: 0;
    background:
      radial-gradient(ellipse 60% 30% at 25% 8%, rgba(150, 120, 200, 0.35), transparent 70%),
      linear-gradient(160deg, transparent 40%, rgba(120, 90, 170, 0.28) 60%, rgba(160, 90, 120, 0.18) 72%, transparent 88%);
  }
</style>
</head>
<body>
<main class="canvas">

  <section class="card card--front" aria-label="Business card front">
    <svg class="front-wave" viewBox="0 0 692 396" aria-hidden="true">
      <path d="M0 294 Q346 414 692 294 L692 396 L0 396 Z" fill="var(--purple-deep)"/>
      <path d="M0 302 Q346 432 692 302 L692 396 L0 396 Z" fill="var(--purple)"/>
    </svg>

    <div class="details">
      <h1 class="holder-name">MARCUS ELLERY</h1>
      <p class="line holder-role">President</p>
      <span class="divider divider--name"></span>

      <p class="line addr-1">The Orchard Court Place</p>
      <p class="line addr-2">Harlow, CM9 4TL, UK</p>
      <span class="divider divider--addr"></span>

      <p class="line line--icon phone">+44 2071958342</p>
      <p class="line line--icon email">info@navelopartnering.com</p>
      <p class="line line--icon web">www.navelopartnering.com</p>
      <span class="divider divider--contact"></span>

      <svg class="contact-icon contact-icon--phone" viewBox="0 0 16 16" aria-hidden="true">
        <path d="M4 1.5 L6 4.5 L4.8 6 C5.6 8 7.6 10.2 9.8 11.2 L11.3 10 L14.3 12 L13 14.5 C7.5 14 2 8.5 1.5 3 Z" fill="var(--purple)"/>
        <path d="M10 2 A4.5 4.5 0 0 1 14 6" stroke="var(--purple)" stroke-width="1.3" fill="none"/>
      </svg>
      <svg class="contact-icon contact-icon--mail" viewBox="0 0 16 16" aria-hidden="true">
        <rect x="1.5" y="3.5" width="13" height="10" rx="1" fill="var(--purple)"/>
        <path d="M2 4 L8 9 L14 4" stroke="var(--white)" stroke-width="1.3" fill="none"/>
      </svg>
      <svg class="contact-icon contact-icon--web" viewBox="0 0 16 16" aria-hidden="true">
        <circle cx="8" cy="8" r="6.5" fill="var(--purple)"/>
        <path d="M1.5 8 H14.5 M8 1.5 C5 5 5 11 8 14.5 M8 1.5 C11 5 11 11 8 14.5" stroke="var(--white)" stroke-width="1" fill="none"/>
      </svg>

      <div class="brand brand--front">
        <span class="brand-dot"></span>
        <span class="brand-name">Navelo</span>
      </div>
    </div>
  </section>

  <section class="card card--back" aria-label="Business card back">
    <div class="back-flow" role="img" aria-label="Soft flowing light lines sweeping across the card"></div>
    <div class="brand brand--back">
      <span class="brand-dot"></span>
      <span class="brand-name">Navelo</span>
    </div>
  </section>

</main>
</body>
</html>
```